Funeral Services Web Site

We need a website for a Funeral Services company. The choice of colors is free of charge. One Page Website with 8 sections. Menu: - Home - Our Services - Obituaries -> link to another page. - Our Shop - Funeral Monument - Funeral Contract - Contact Us

Target Market(s)

Every one need Funeral Services

Coding

Coded - Design and coding required

Number of Pages Required

2 page

Font styles to use
Sans Serif
Script

Colors

Designer to choose colors to be used in the design.

```html
<!DOCTYPE html>
<html lang="en">
<head>
<meta charset="utf-8">
<title>Maison Lavelle – Funeral Services</title>
<link href="https://fonts.googleapis.com/css2?family=Libre+Baskerville:wght@700&family=Raleway:wght@400;500;600;700&display=swap" rel="stylesheet">
<style>
:root{
  --brown:#7b6548;
  --brown-dark:#5f4d36;
  --ink:#222;
  --text:#555;
  --grey-card:#9a9a9a;
  --light:#efefef;
  --footer:#f4f4f4;
  --white:#fff;
}
*{box-sizing:border-box;margin:0;padding:0}
html,body{width:1200px;height:4662px;overflow:hidden}
body{position:relative;font-family:"Raleway",sans-serif;color:var(--text);background:var(--white);font-size:13px}
.abs{position:absolute}
a{color:inherit;text-decoration:none}
.btn{position:absolute;display:flex;align-items:center;justify-content:center;gap:6px;font-size:11.5px;font-weight:600}
.btn-fill{background:var(--brown);color:var(--white)}
.btn-line{border:1.5px solid var(--brown);color:var(--brown-dark);background:var(--white)}
.section-title{position:absolute;left:0;width:1200px;text-align:center;font-weight:700;font-size:31px;color:var(--ink);letter-spacing:.5px}
.logo{display:flex;align-items:center;gap:10px;font-weight:700;color:var(--brown);font-size:22px}
.logo .mark{width:34px;height:34px;border:2px solid var(--brown);border-radius:50%}
.photo{position:absolute}

/* header */
.topline{left:0;top:0;width:1200px;height:4px;background:var(--brown)}
.topbar{left:700px;top:4px;width:500px;height:38px;background:var(--brown);clip-path:polygon(0 0,100% 0,100% 100%,8% 100%)}
.nav{left:410px;top:70px;display:flex;gap:31px;font-size:12.5px;font-weight:500;color:#333}
.nav .active{color:var(--brown)}
.social{display:flex;gap:8px}
.social span{width:26px;height:26px;border:1.5px solid var(--white);border-radius:50%}

/* hero */
.hero{left:0;top:128px;width:1200px;height:537px;background:linear-gradient(90deg,#0b0b0b 0%,#1a1a1a 35%,#4a4a44 60%,#8a8070 80%,#6a7a55 100%)}
.hero h1{position:absolute;left:145px;top:160px;font-family:"Libre Baskerville",serif;font-size:32px;line-height:43px;color:var(--white)}
.hero p{position:absolute;left:143px;top:254px;width:330px;font-size:13px;line-height:24px;color:#eee}

/* services */
.svc-col{position:absolute;top:1410px;width:210px;text-align:center}
.svc-col .circ{width:200px;height:200px;border-radius:50%;border:4px solid var(--white);margin:0 auto;box-shadow:0 2px 8px rgba(0,0,0,.2)}
.svc-col h3{font-size:12.5px;font-weight:700;color:#333;margin-top:30px;line-height:18px}
.svc-col p{font-size:13px;line-height:20px;margin-top:18px;color:#555}
.arrow{position:absolute;width:38px;height:38px;border:1.5px solid var(--brown);border-radius:50%;background:var(--white);display:flex;align-items:center;justify-content:center}

/* contract */
.plan{position:absolute;background:var(--white);box-shadow:0 1px 4px rgba(0,0,0,.08)}
.plan .head{background:var(--grey-card);color:var(--white);text-align:center;padding-top:35px}
.plan.mid .head{background:var(--brown)}
.plan .head h4{font-size:19px;font-weight:600}
.plan .head .disc{font-size:14px;margin-top:10px}
.plan .head .price{font-size:22px;font-weight:700;margin-top:6px}
.plan .head .inc{font-size:14px;margin-top:6px}
.plan ul{list-style:none;padding:16px 30px 0}
.plan li{font-size:12px;color:#444;border-bottom:1px solid #e4e4e4;padding:9px 0 8px;line-height:16px}

/* obituaries */
.obit-face{position:absolute;top:3677px;width:131px;height:151px;display:flex;align-items:flex-end;justify-content:center;padding-bottom:10px;font-size:11px;font-weight:700;color:var(--white)}

/* contact */
.field{position:absolute;border:1px solid #d8d8d8;font-size:11px;color:#888;padding:12px 12px;display:flex;justify-content:space-between}

/* footer */
.foot-h{font-weight:700;font-size:15px;color:#222}
.foot-list{list-style:disc;padding-left:18px;font-size:12.5px;line-height:27px;color:#444}
</style>
</head>
<body>

<!-- Header -->
<div class="abs topline"></div>
<div class="abs topbar"></div>
<div class="abs" style="left:620px;top:11px;font-size:11px;color:#333;display:flex;align-items:center;gap:5px">
  <span style="width:22px;height:14px;background:#2c3e7a;display:inline-block"></span>ENG ▾
</div>
<div class="abs" style="left:768px;top:10px;display:flex;align-items:center;gap:8px;color:var(--white);font-size:12px;font-weight:600">
  <svg width="24" height="24" viewBox="0 0 24 24"><circle cx="12" cy="12" r="11" fill="none" stroke="#fff" stroke-width="1.5"/><path d="M8 7l2 0 1 3-1.5 1a7 7 0 0 0 3 3l1-1.5 3 1 0 2c-5 1-9-3-8.5-8.5z" fill="#fff"/></svg>
  123.456.7890
</div>
<div class="abs social" style="left:920px;top:8px"><span></span><span></span><span></span><span></span></div>
<div class="abs logo" style="left:145px;top:35px"><span>Maison Lavelle</span><span class="mark"></span></div>
<nav class="abs nav">
  <a class="active">Home</a><a>Services</a><a>Obituaries</a><a>Our Shop</a><a>Funeral Monument</a><a>Funeral Contract</a><a>Contact</a>
</nav>

<!-- Hero -->
<section class="abs hero" role="img" aria-label="Candles and a funeral urn with white flowers, a hand resting on the urn">
  <h1>Helping You Cope<br>With Grief</h1>
  <p>We explain some of the feelings you may have &amp; suggest ways of dealing with them.</p>
  <a class="btn btn-fill" style="left:141px;top:333px;width:155px;height:32px">Contact Us Today →</a>
</section>

<!-- About -->
<div class="abs" style="left:467px;top:766px;font-size:30px;font-weight:700;color:var(--ink)">About</div>
<div class="abs logo" style="left:585px;top:768px;font-size:20px"><span>Maison Lavelle</span><span class="mark" style="width:28px;height:28px"></span></div>
<div class="abs" style="left:142px;top:903px;width:430px;font-size:13px;font-weight:700;color:var(--brown);line-height:20px">Duis autem vel eum iriure dolor in hendrerit in vulputate velit esse molestie consequat, vel illum.</div>
<div class="abs" style="left:142px;top:960px;width:455px;font-size:12px;line-height:20.5px;color:#444">Lorem ipsum dolor sit amet, consectetuer adipiscing elit, sed diamond cut a nonummy nibh euismod tincidunt ut laoreet dolore magna aliquam eratmori volutpat. Ut wisi enim ad minim veniam, quis nostrud exerci tation ullamcorl suscipit lobortis nisl ut aliquip ex ea commodo consequat. At vero eros etnk accumsan et iusto odio dignissim quom facilisi.</div>
<a class="btn btn-line" style="left:141px;top:1079px;width:141px;height:31px">Contact Us Today →</a>
<div class="photo" style="left:628px;top:863px;width:430px;height:292px;background:var(--white);box-shadow:0 2px 10px rgba(0,0,0,.18)"></div>
<div class="photo" role="img" aria-label="Funeral director in a suit standing beside wooden caskets" style="left:635px;top:869px;width:417px;height:280px;background:linear-gradient(90deg,#c69a60,#8a6a45 40%,#2b2b2b 55%,#b88d5a 80%,#d8b88a)"></div>

<!-- Services -->
<div class="photo" role="img" aria-label="Dim chapel interior with wooden pews" style="left:0;top:1241px;width:1200px;height:269px;background:linear-gradient(90deg,#3a2a20,#5a4030 30%,#2a201a 60%,#4a3525)"></div>
<div class="abs" style="left:0;top:1241px;width:1200px;height:269px;background:rgba(20,15,10,.45)"></div>
<div class="section-title" style="top:1328px;color:var(--white)">Our Services</div>
<div class="arrow" style="left:76px;top:1491px"><svg width="16" height="10"><path d="M15 5H2M5 1L1 5l4 4" stroke="#7b6548" stroke-width="1.5" fill="none"/></svg></div>
<div class="arrow" style="left:1086px;top:1491px"><svg width="16" height="10"><path d="M1 5h13M11 1l4 4-4 4" stroke="#7b6548" stroke-width="1.5" fill="none"/></svg></div>
<div class="svc-col" style="left:142px">
  <div class="circ" role="img" aria-label="Two hands holding each other in comfort" style="background:radial-gradient(circle,#c8a890,#7a5a48)"></div>
  <h3>Personalized &amp; Dignified Support<br>From The First Moments</h3>
  <p>Lorem ipsum dolor sit amet, consectetuer adipiscing elit, sed diamond cut nonummy nibh euismod tincidunt ut.</p>
</div>
<div class="svc-col" style="left:379px">
  <div class="circ" role="img" aria-label="Family members sitting together reviewing papers" style="background:radial-gradient(circle,#e8e0d4,#a89880)"></div>
  <h3>Assistance In All Administrative<br>Procedures</h3>
  <p>Lorem ipsum dolor sit amet, consectetuer adipiscing elit, sed diamond cut nonummy nibh euismod tincidunt ut.</p>
</div>
<div class="svc-col" style="left:616px">
  <div class="circ" role="img" aria-label="A red rose resting on piano keys" style="background:radial-gradient(circle,#d01820 0 25%,#333 45%,#1a1a1a)"></div>
  <h3>Offer Him His Song To Pay Him<br>A Last Tribute</h3>
  <p>Lorem ipsum dolor sit amet, consectetuer adipiscing elit, sed diamond cut nonummy nibh euismod tincidunt ut.</p>
</div>
<div class="svc-col" style="left:852px">
  <div class="circ" role="img" aria-label="Birds flying over the sea at an orange sunset" style="background:linear-gradient(180deg,#e85a10,#f8a020 55%,#3a2010 75%,#1a1008)"></div>
  <h3>Put Down Your Last Wishes To<br>Guarantee Their Respect!</h3>
  <p>Lorem ipsum dolor sit amet, consectetuer adipiscing elit, sed diamond cut nonummy nibh euismod tincidunt ut.</p>
</div>
<a class="btn btn-line" style="left:529px;top:1802px;width:142px;height:31px">Contact Us Today →</a>

<!-- Shop -->
<div class="photo" role="img" aria-label="White roses beside a polished casket" style="left:0;top:1918px;width:1200px;height:388px;background:linear-gradient(90deg,#c8cfa8,#8a9a68 25%,#d8c8a8 45%,#6a5a48 60%,#222 70%)"></div>
<svg class="abs" style="left:0;top:1918px" width="1200" height="388" viewBox="0 0 1200 388">
  <polygon points="640,0 1200,0 1200,388 780,388 540,178" fill="#1e1e1e"/>
  <polygon points="640,0 650,0 550,178 790,388 780,388 540,178" fill="#7b6548"/>
</svg>
<div class="abs" style="right:143px;top:2026px;font-size:29px;font-weight:700;color:var(--white)">Our Shop</div>
<div class="abs" style="left:675px;top:2074px;width:382px;text-align:right;font-size:15px;line-height:25px;color:#ddd">Adjacent to our funeral home and accessible by Alder Lane West, our store offers a wide selection of silk flowers and funeral items.</div>
<a class="btn btn-fill" style="left:945px;top:2173px;width:113px;height:30px">Shop Now →</a>

<!-- Funeral Monument -->
<div class="section-title" style="top:2387px">Funeral Monument</div>
<div class="arrow" style="left:76px;top:2641px"><svg width="16" height="10"><path d="M15 5H2M5 1L1 5l4 4" stroke="#7b6548" stroke-width="1.5" fill="none"/></svg></div>
<div class="arrow" style="left:1086px;top:2641px"><svg width="16" height="10"><path d="M1 5h13M11 1l4 4-4 4" stroke="#7b6548" stroke-width="1.5" fill="none"/></svg></div>
<div class="photo" role="img" aria-label="Open casket with flowers in a viewing room" style="left:141px;top:2455px;width:220px;height:180px;background:linear-gradient(135deg,#e8dcc8,#8a3a20 60%,#c8b898)"></div>
<div class="photo" role="img" aria-label="Mourners gathered around flowers" style="left:141px;top:2648px;width:220px;height:218px;background:linear-gradient(135deg,#5a4a40,#c8c0b8 50%,#6a5a58)"></div>
<div class="photo" role="img" aria-label="Cemetery gravestone at dusk" style="left:375px;top:2455px;width:220px;height:243px;background:linear-gradient(#3a3a30,#1a1a18)"></div>
<div class="abs" style="left:375px;top:2455px;width:220px;height:243px;background:rgba(0,0,0,.55);display:flex;flex-direction:column;align-items:center;justify-content:center;color:#ddd;font-size:13px;text-align:center;line-height:20px">
  <svg width="38" height="38" style="margin-bottom:14px"><circle cx="19" cy="19" r="17" fill="none" stroke="#ddd" stroke-width="1.5"/><path d="M19 12v14M12 19h14" stroke="#ddd" stroke-width="1.5"/></svg>
  Consectetuer Adipiscing<br>Sed Diam Nonummy
</div>
<div class="photo" role="img" aria-label="Stone crosses in a grassy cemetery" style="left:375px;top:2710px;width:220px;height:156px;background:linear-gradient(#6a8a40,#8a8a80 50%,#5a7a38)"></div>
<div class="photo" role="img" aria-label="Red wooden casket with a flower spray" style="left:606px;top:2455px;width:220px;height:155px;background:linear-gradient(#e8e4e0,#8a2a18 55%,#d8d0c8)"></div>
<div class="photo" role="img" aria-label="Headstone surrounded by green shrubs" style="left:606px;top:2622px;width:220px;height:244px;background:linear-gradient(90deg,#4a6a28,#a8a090 50%,#3a5a20)"></div>
<div class="photo" role="img" aria-label="Flower resting on a wooden casket lid" style="left:838px;top:2455px;width:220px;height:217px;background:linear-gradient(#4a7a28,#8a5a30 60%,#c87a40)"></div>
<div class="photo" role="img" aria-label="White headstone with red flowers on a lawn" style="left:838px;top:2686px;width:220px;height:180px;background:linear-gradient(#8aa068,#e8e8e0 45%,#5a8a38)"></div>

<!-- Funeral Contract -->
<div class="abs" style="left:0;top:2950px;width:1200px;height:727px;background:var(--light)"></div>
<div class="section-title" style="top:3023px">Funeral Contract</div>
<div class="plan" style="left:141px;top:3137px;width:300px;height:429px">
  <div class="head" style="height:183px"><h4>Simple Plan</h4><div class="disc">($50 online discount)</div><div class="price">$ 2300</div><div class="inc">Inculded in the Plan</div></div>
  <ul><li>$ 500.00 Advice and guidance on all funeral</li><li>$ 800.00 Cremation or Burial</li><li>$ 400.00 The coffin</li><li>$ 200.00 Service at local crematorium</li><li>$ 400.00 Full listing of floral tributes</li><li>$ 000.00 Free cancellation period</li></ul>
</div>
<div class="plan" style="left:759px;top:3137px;width:300px;height:429px">
  <div class="head" style="height:183px"><h4>Simple Plan</h4><div class="disc">($50 online discount)</div><div class="price">$ 2300</div><div class="inc">Inculded in the Plan</div></div>
  <ul><li>$ 500.00 Advice and guidance on all funeral</li><li>$ 800.00 Cremation or Burial</li><li>$ 400.00 The coffin</li><li>$ 200.00 Service at local crematorium</li><li>$ 400.00 Full listing of floral tributes</li><li>$ 000.00 Free cancellation period</li></ul>
</div>
<div class="plan mid" style="left:440px;top:3108px;width:320px;height:500px;box-shadow:0 2px 12px rgba(0,0,0,.15)">
  <div class="head" style="height:183px"><h4>Mid-range Plan</h4><div class="disc">($50 online discount)</div><div class="price">$ 3500</div><div class="inc">Inculded in the Plan</div></div>
  <ul><li>$ 500.00 Advice and guidance on all funeral</li><li>$ 800.00 Cremation or Burial</li><li>$ 400.00 The coffin</li><li>$ 200.00 Service at local crematorium</li><li>$ 400.00 Full listing of floral tributes</li><li>$ 000.00 Free cancellation period</li></ul>
</div>
<a class="btn btn-fill" style="left:544px;top:3582px;width:112px;height:30px">Get Started →</a>

<!-- Recent Obituaries -->
<div class="abs" style="left:0;top:3677px;width:1200px;height:151px;background:var(--brown)"></div>
<div class="abs" style="left:142px;top:3698px;font-size:19px;font-weight:700;color:var(--white)">Recent Obituaries</div>
<div class="abs" style="left:142px;top:3733px;width:240px;font-size:11px;line-height:17px;color:#e8dcc8">Lorem ipsum dolor sit amet, consectetuer adipiscing elit it dues owner ipsum.</div>
<div class="abs" style="left:142px;top:3783px;display:flex;gap:4px">
  <span style="width:18px;height:18px;background:#111;color:#fff;font-size:11px;display:flex;align-items:center;justify-content:center">‹</span>
  <span style="width:18px;height:18px;background:#111;color:#fff;font-size:11px;display:flex;align-items:center;justify-content:center">›</span>
</div>
<div class="obit-face" role="img" aria-label="Portrait of Marco Bellini" style="left:402px;background:linear-gradient(#8a8a88,#3a3a38)">Marco BELLINI</div>
<div class="obit-face" role="img" aria-label="Portrait of Odette Marais" style="left:533px;background:linear-gradient(#b8a898,#6a5848);flex-direction:column;align-items:center;font-size:10px;line-height:15px"><span>Odette MARAIS</span><span style="font-weight:400">Apr 12, 2020</span><span style="font-weight:400">Vallon-sur-Lys</span></div>
<div class="obit-face" role="img" aria-label="Portrait of Lucien" style="left:664px;background:linear-gradient(#6a6a68,#2a2a28)">Lucien</div>
<div class="obit-face" role="img" aria-label="Portrait of Henri" style="left:795px;background:linear-gradient(#9a9a90,#4a4a40)">Henri</div>
<div class="obit-face" role="img" aria-label="Portrait of Paolo Ruiz" style="left:926px;background:linear-gradient(#7a6a60,#3a2a20)">Paolo Ruiz</div>

<!-- Contact -->
<div class="section-title" style="top:3924px">Contact Us</div>
<div class="field" style="left:301px;top:4040px;width:290px;height:41px"><span>Your Name*</span><span>👤︎</span></div>
<div class="field" style="left:635px;top:4040px;width:290px;height:41px"><span>Your Email*</span><span>✉︎</span></div>
<div class="field" style="left:301px;top:4096px;width:290px;height:41px"><span>Your Phone*</span><span>☏︎</span></div>
<div class="field" style="left:635px;top:4096px;width:290px;height:41px"><span>Inquiry For*</span><span>⌄</span></div>
<div class="field" style="left:301px;top:4152px;width:624px;height:82px"><span>Your Message*</span><span>…</span></div>
<a class="btn btn-fill" style="left:543px;top:4248px;width:112px;height:31px;font-size:13px">Submit →</a>

<!-- Footer -->
<div class="abs" style="left:0;top:4345px;width:1200px;height:285px;background:var(--footer)"></div>
<div class="abs" style="left:142px;top:4383px"><div class="foot-h">Quick Links</div>
  <div style="width:165px;height:1px;background:#ccc;margin:10px 0 6px"></div>
  <ul class="foot-list"><li style="color:var(--brown)">Home</li><li>About Us</li><li>Services</li><li>Jobs</li><li>Reviews</li><li>Contact Us</li></ul>
</div>
<div class="abs" style="left:352px;top:4383px;width:1px;height:200px;background:#ddd"></div>
<div class="abs" style="left:452px;top:4383px;width:320px"><div class="foot-h">Contact Details</div>
  <div style="width:200px;height:1px;background:#ccc;margin:10px 0 14px"></div>
  <div style="display:flex;gap:14px;font-size:12px;line-height:18px;color:#444">
    <svg width="28" height="28" viewBox="0 0 28 28"><circle cx="14" cy="14" r="14" fill="#7b6548"/><path d="M14 7a5 5 0 0 0-5 5c0 4 5 9 5 9s5-5 5-9a5 5 0 0 0-5-5z" fill="#fff"/><circle cx="14" cy="12" r="1.8" fill="#7b6548"/></svg>
    <div><b style="color:var(--brown)">Maison Lavelle</b><br>121 Street Name, City Name<br>State - Zipcode</div>
  </div>
  <div style="display:flex;gap:14px;align-items:center;font-size:12px;color:#444;margin-top:18px">
    <svg width="28" height="28" viewBox="0 0 28 28"><circle cx="14" cy="14" r="14" fill="#7b6548"/><path d="M10 9h2.5l1 3-1.5 1a6 6 0 0 0 3 3l1-1.5 3 1V18c-5 1-9-3-9-9z" fill="#fff"/></svg>123.456.7890</div>
  <div style="display:flex;gap:14px;align-items:center;font-size:12px;color:#444;margin-top:14px">
    <svg width="28" height="28" viewBox="0 0 28 28"><circle cx="14" cy="14" r="14" fill="#7b6548"/><rect x="8" y="10" width="12" height="8" fill="#fff"/><path d="M8 10l6 5 6-5" stroke="#7b6548" fill="none"/></svg>info@maisonlavelle.com</div>
</div>
<div class="abs" style="left:773px;top:4383px;width:1px;height:200px;background:#ddd"></div>
<div class="abs logo" style="left:873px;top:4490px"><span>Maison Lavelle</span><span class="mark"></span></div>

<div class="abs" style="left:0;top:4630px;width:1200px;height:32px;background:var(--brown)"></div>
<div class="abs" style="left:142px;top:4640px;font-size:11px;color:#eee">Copyright 2019 Maison Lavelle. All Rights Reserved</div>
<div class="abs social" style="left:956px;top:4633px"><span></span><span></span><span></span></div>

</body>
</html>
```